Life Coaching and Career Coaching company needs new website with bold, modern, videos

We need a whole new website that is heavy on video. We are a small company who sells personal wellbeing services like career coaching, life coaching, and group coaching programs. The programs all help people design a better life.
FULL BRIEF ATTACHED and STYLE GUIDE
Also, look at https://www.brightfennel.com/coaching and galdrove.com and https://www.marnwick.life/ for a small amount of inspiration.

Industry/Entity Type

personal well-being/life coaching/career coaching

Number of Pages Required

3 page

Other font styles liked:
• fonts are in the brief

Requirements
Must have
• read the brief please - it's all in there. (things like the look, feel, how it will have lots of video, etc,)
Nice to have
• something really different looking and breakthrough. visually stunning. very trustworthy. Please read the brief, its all in there.
Should not have
• should not look like other life coaching websites. must have video!

```html
<!DOCTYPE html>
<html lang="en">
<head>
<meta charset="utf-8">
<title>Kindred Path Project</title>
<link href="https://fonts.googleapis.com/css2?family=Playfair+Display:wght@600;700&family=Poppins:wght@400;500;600&display=swap" rel="stylesheet">
<style>
:root{
  --teal:#03565a;
  --teal-bright:#2bb3b8;
  --coral:#ef5f5c;
  --pink:#fdf1f1;
  --ink:#2b2b2b;
  --dark:#2e2e2e;
  --muted:#6b6b6b;
  --line:#e6e6e6;
  --field:#f2f3f3;
  --page:#efeeef;
  --white:#fff;
}
*{box-sizing:border-box;margin:0;padding:0}
html,body{width:1200px;height:2581px;overflow:hidden;background:var(--page)}
body{font-family:'Poppins',sans-serif;color:var(--ink)}
.site{position:absolute;left:283px;top:47px;width:634px;background:var(--white)}
section,header,footer{position:relative;width:634px;overflow:hidden}
.abs{position:absolute}
.serif{font-family:'Playfair Display',serif;font-weight:700}
.hl{color:var(--teal)}
.hl-coral{color:var(--coral)}
.eyebrow{font-size:7px;font-weight:500;color:var(--teal)}
.btn{position:absolute;display:flex;align-items:center;justify-content:center;border-radius:14px;font-size:6.5px;font-weight:600;gap:3px}
.btn-teal{background:var(--teal);color:#fff}
.btn-grey{background:#9a9a9a;color:#fff}
.btn-white{background:#fff;color:var(--teal)}
.media{position:absolute;border-radius:6px;overflow:hidden}
.play{position:absolute;width:0;height:0;border-top:11px solid transparent;border-bottom:11px solid transparent;border-left:19px solid var(--coral)}
.caption{position:absolute;font-size:7.5px;color:#fff;font-weight:500}
/* nav */
.nav{height:50px;border-bottom:1px solid var(--line);background:linear-gradient(90deg,#fff 226px,var(--pink) 226px)}
.brand{position:absolute;left:62px;top:18px;font-size:12px;font-weight:500;color:var(--teal);letter-spacing:.3px}
.nav-links{position:absolute;left:211px;top:21px;display:flex;gap:14px;font-size:6.5px;color:var(--muted)}
.nav-links .active{color:var(--teal);font-weight:500;border-bottom:1.5px solid var(--teal);padding-bottom:2px}
/* hero */
.hero{height:298px}
.hero-band{position:absolute;left:226px;top:0;width:408px;height:202px;background:var(--pink)}
.hero h1{position:absolute;left:62px;top:31px;font-size:26px;line-height:35px;width:420px}
.hero p{position:absolute;left:62px;top:112px;width:192px;font-size:6.4px;line-height:11.5px;color:var(--muted)}
/* about */
.about{height:264px;text-align:center}
.about .eyebrow{position:absolute;top:24px;width:100%}
.center-h{position:absolute;left:0;width:100%;font-size:18.5px;line-height:27px}
.quote{position:absolute;width:100%;font-size:6.6px;color:var(--muted);line-height:11px}
.para{position:absolute;font-size:6.6px;color:var(--muted);line-height:12px}
/* solutions */
.solutions{height:485px;background:var(--teal);color:#fff}
.solutions .eyebrow{color:var(--coral);position:absolute;left:62px;top:48px}
.solutions h2{position:absolute;left:62px;top:66px;width:330px;font-size:18.5px;line-height:27.5px}
.solutions .para{left:62px;top:154px;width:334px;color:#d6e8e8}
.arrow{position:absolute;width:26px;height:18px}
.pager{position:absolute;left:272px;top:440px;width:90px;height:1px;background:#8fb6b6}
.pager i{position:absolute;left:16px;top:-1px;width:24px;height:3px;border-radius:2px;background:#fff}
/* testimonials */
.voices{height:747px;background:linear-gradient(180deg,#fff 325px,var(--dark) 325px);text-align:center}
.voices .eyebrow{position:absolute;top:89px;width:100%}
.pill{position:absolute;top:660px;width:114px;height:26px;border:1px solid #fff;border-radius:14px;color:#fff;font-size:7px;display:flex;align-items:center;justify-content:center}
.pill.on{background:#fff;color:var(--coral)}
/* contact */
.contact{height:424px}
.contact .eyebrow{position:absolute;left:62px;top:58px}
.contact h2{position:absolute;left:62px;top:72px;width:215px;font-size:18.5px;line-height:27.5px}
.contact .para{left:62px;top:194px;width:250px}
.contact-row{position:absolute;left:62px;display:flex;align-items:center;gap:14px;font-size:7.5px}
.form{position:absolute;left:342px;top:61px;width:226px;height:320px;background:#fff;border-radius:8px;box-shadow:0 6px 24px rgba(0,0,0,.08)}
.form h3{position:absolute;left:27px;top:26px;font-size:11px;font-weight:500}
.field{position:absolute;background:var(--field);border-radius:2px;font-size:6px;color:#a0a0a0;padding:7px}
/* footer */
.footer{height:218px;background:var(--teal);color:#fff}
.footer .brand{color:#fff;top:44px;font-size:15px}
.footer-desc{position:absolute;left:62px;top:86px;width:125px;font-size:6.5px;line-height:10.5px;color:#cfe3e3}
.col{position:absolute;top:46px;font-size:6.5px;line-height:17px;color:#cfe3e3}
.col b{display:block;color:#fff;font-weight:600;line-height:14px;margin-bottom:6px;font-size:7px}
.rule{position:absolute;left:30px;right:30px;top:175px;height:1px;background:#2f7a7d}
.copy{position:absolute;right:62px;top:192px;font-size:6px;color:#cfe3e3}
</style>
</head>
<body>
<div class="site">

  <header class="nav">
    <div class="brand">Kindred Path</div>
    <nav class="nav-links">
      <span class="active">Home</span><span>About us</span><span>Solutions</span><span>Resources ⌄</span><span>Testimonials</span><span>Blogs</span>
    </nav>
    <div class="btn btn-teal" style="left:499px;top:13px;width:72px;height:24px">Get Started</div>
  </header>

  <section class="hero">
    <div class="hero-band"></div>
    <h1 class="serif">Unleash Your <span class="hl">Potential</span>, Unleash Your <span class="hl">Power.</span></h1>
    <p>Unlock your potential with personalized coaching services tailored to your unique journey. At Kindred Path Project, we are dedicated to helping you design the life you deserve through transformative programs that foster personal growth and empowerment. Embrace change, thrive, and cultivate holistic well-being</p>
    <div class="btn btn-teal" style="left:62px;top:208px;width:80px;height:24px">Get Started ↗</div>
    <div class="btn btn-grey" style="left:149px;top:208px;width:80px;height:24px">Watch Demo ↗</div>
    <div class="media" role="img" aria-label="Video still: two people talking across a table in a bright office, teal tint" style="left:277px;top:73px;width:294px;height:185px;background:linear-gradient(135deg,#3fc4c7,#1e9ea3 60%,#137a7f)">
      <div class="play" style="left:138px;top:81px"></div>
      <div class="caption" style="left:13px;top:160px">Watch project demo (04:21)</div>
    </div>
  </section>

  <section class="about">
    <div class="eyebrow">About the Kindred Path Project</div>
    <h2 class="serif center-h" style="top:38px;font-weight:600">Our Journey of Empowerment:<br>Unveiling the Heart and Soul Behind<br>Our Holistic <span class="hl">Well-being</span> Mission.</h2>
    <div class="quote" style="top:132px">"SUCCESS IS NOT FINAL, FAILURE IS NOT FATAL: IT IS THE COURAGE<br>TO CONTINUE THAT COUNTS."</div>
    <div class="para" style="top:166px;left:185px;width:264px">Driven by the belief that everyone deserves to lead a purposeful life, we are on a mission to ignite positive transformations. Our commitment to nurturing personal growth and well-being is at the heart of everything we do.</div>
  </section>

  <section class="solutions">
    <div class="eyebrow">Discover Our Solutions</div>
    <h2 class="serif" style="font-weight:600">Discover Tailored and Innovative Solutions Crafted Just for You by Our Expert Team.</h2>
    <div class="btn btn-white" style="left:499px;top:88px;width:72px;height:24px">Get Started</div>
    <div class="para">Our expert team is dedicated to crafting tailored and innovative solutions designed to elevate your success. We strive to transcend the ordinary and make a tangible impact, ensuring that you receive nothing short of exceptional results. Explore our array of services and unlock the potential for transformative growth and success.</div>
    <div class="media" role="img" aria-label="Photo: person standing on a mountain top under a cloudy sky" style="left:-6px;top:240px;width:157px;height:167px;background:linear-gradient(180deg,#7d98ad,#5a7488 60%,#3e4e58)"></div>
    <svg class="arrow" style="left:60px;top:315px" viewBox="0 0 26 18"><path d="M25 9H2M10 1L2 9l8 8" fill="none" stroke="#fff" stroke-width="1.6"/></svg>
    <div class="media" role="img" aria-label="Video still: coach and client talking in a meeting room with a brick wall" style="left:162px;top:232px;width:309px;height:184px;background:linear-gradient(135deg,#d9a48c,#c88f79 55%,#4a4f5e)">
      <div class="caption" style="right:20px;top:14px;font-size:7px">Watch video (02:51)</div>
      <div class="play" style="left:145px;top:81px"></div>
      <div class="caption" style="left:20px;top:161px;font-size:8.5px">career coaching</div>
      <div class="caption" style="right:20px;top:163px;font-size:6.5px">See more →</div>
    </div>
    <div class="media" role="img" aria-label="Photo: woman smiling in a modern office with a neon sign" style="left:481px;top:240px;width:160px;height:167px;background:linear-gradient(135deg,#3b4a4d,#7e8f8f 60%,#b9a28e)"></div>
    <svg class="arrow" style="left:544px;top:315px" viewBox="0 0 26 18"><path d="M1 9h23M16 1l8 8-8 8" fill="none" stroke="#fff" stroke-width="1.6"/></svg>
    <div class="pager"><i></i></div>
  </section>

  <section class="voices">
    <div class="eyebrow">Discover Our Solutions</div>
    <h2 class="serif center-h" style="top:105px;font-weight:600">Voices of Success: Real Stories, <span class="hl">Real</span><br><span class="hl">Impact</span> - Hear Directly from Our<br>Satisfied Clients.</h2>
    <div class="quote" style="top:196px;left:175px;width:284px">"THE ONLY LIMIT TO OUR REALIZATION OF TOMORROW WILL BE OUR DOUBTS OF TODAY."</div>
    <div class="para" style="top:229px;left:150px;width:334px">Hear firsthand how our tailored solutions have transformed their businesses and unlocked new levels of success.</div>
    <div class="media" role="img" aria-label="Portrait of a bearded client, teal tint" style="left:36px;top:281px;width:76px;height:185px;background:linear-gradient(180deg,#2fa5a9,#146c70)"></div>
    <svg class="arrow" style="left:60px;top:364px" viewBox="0 0 26 18"><path d="M25 9H2M10 1L2 9l8 8" fill="none" stroke="#fff" stroke-width="1.6"/></svg>
    <div class="media" role="img" aria-label="Video still: smiling client with glasses on a light grey backdrop" style="left:120px;top:281px;width:307px;height:185px;background:linear-gradient(135deg,#eceeef,#d6d9db)">
      <div class="abs serif" style="left:24px;top:2px;font-size:52px;color:#222">”</div>
      <div class="play" style="left:140px;top:80px"></div>
      <div class="caption" style="left:13px;top:160px;color:#333;font-size:7px">Watch testimonial (02:51)</div>
    </div>
    <div class="media" role="img" aria-label="Portrait of a client in a jacket, teal tint" style="left:435px;top:281px;width:77px;height:185px;background:linear-gradient(180deg,#2b8d7e,#1b5d55)"></div>
    <div class="media" role="img" aria-label="Portrait of a smiling client, teal tint" style="left:521px;top:281px;width:76px;height:185px;background:linear-gradient(180deg,#35b0b3,#176e72)"></div>
    <svg class="arrow" style="left:546px;top:364px" viewBox="0 0 26 18"><path d="M1 9h23M16 1l8 8-8 8" fill="none" stroke="#fff" stroke-width="1.6"/></svg>
    <div class="media" role="img" aria-label="Portrait of a client, teal tint" style="left:606px;top:281px;width:34px;height:185px;background:linear-gradient(180deg,#2ea2a6,#155f63)"></div>
    <h2 class="serif center-h" style="top:528px;color:#fff;font-weight:600">Elevating Success: Embracing Creativity<br>to Breathe Life into <span class="hl-coral">Dreams</span> and<br>Transform Visions into <span class="hl-coral">Reality.</span></h2>
    <div class="para" style="top:618px;left:170px;width:294px;color:#ddd">Our coaching website is your gateway to unlocking potential, realizing dreams, and achieving unparalleled success. Embrace creativity, redefine success, and elevate your life today.</div>
    <div class="pill" style="left:124px">LIFE COACHING</div>
    <div class="pill" style="left:260px">CAREER COACHING</div>
    <div class="pill on" style="left:396px">GROUP COACHING</div>
  </section>

  <section class="contact">
    <div class="eyebrow">Contact Us</div>
    <h2 class="serif" style="font-weight:600">Joining Hands: Building Relationships, and Enriching Lives - Reach Out to Us Today.</h2>
    <div class="para">We welcome the opportunity to engage with you. Whether you have questions, innovative ideas to share, or simply wish to extend a friendly greeting, our doors are open, and our ears are ready to listen. Feel free to reach out to us via a message, a phone call, or by visiting us in person. We eagerly anticipate the chance to connect with you.</div>
    <div class="contact-row" style="top:290px"><svg width="9" height="7" viewBox="0 0 9 7"><rect width="9" height="7" rx="1" fill="#03565a"/><path d="M0.5 0.8L4.5 4 8.5 0.8" fill="none" stroke="#fff" stroke-width=".8"/></svg>hello@kindredpathproject.com</div>
    <div class="contact-row" style="top:309px"><svg width="9" height="9" viewBox="0 0 24 24"><path d="M6.6 10.8a15 15 0 006.6 6.6l2.2-2.2a1 1 0 011-.25 11.4 11.4 0 003.6.57 1 1 0 011 1V20a1 1 0 01-1 1A17 17 0 013 4a1 1 0 011-1h3.5a1 1 0 011 1 11.4 11.4 0 00.57 3.6 1 1 0 01-.25 1z" fill="#03565a"/></svg>00 254 000 1234</div>
    <div class="contact-row" style="top:328px"><svg width="9" height="9" viewBox="0 0 10 10"><circle cx="5" cy="5" r="4" fill="none" stroke="#03565a" stroke-width="1.2"/><circle cx="5" cy="5" r="1.6" fill="#03565a"/></svg>14 Ember Lane, Westbrook, NE</div>
    <div class="form">
      <h3>Let's get in touch</h3>
      <div class="btn btn-teal" style="left:27px;top:54px;width:176px;height:24px;border-radius:3px">Get started now</div>
      <div class="abs" style="left:27px;top:97px;width:176px;height:1px;background:var(--line)"></div>
      <div class="abs" style="left:107px;top:93px;width:16px;background:#fff;text-align:center;font-size:5px;color:#aaa">or</div>
      <div class="field" style="left:27px;top:111px;width:84px;height:24px">First Name</div>
      <div class="field" style="left:119px;top:111px;width:84px;height:24px">Last Name</div>
      <div class="field" style="left:27px;top:142px;width:176px;height:24px">Email Adress</div>
      <div class="field" style="left:27px;top:173px;width:176px;height:24px">Phone Number</div>
      <div class="field" style="left:27px;top:204px;width:176px;height:63px">Tell us how we can help you</div>
      <div class="btn btn-teal" style="left:27px;top:282px;width:64px;height:24px;border-radius:3px">Send</div>
    </div>
  </section>

  <footer class="footer">
    <div class="brand">Kindred Path</div>
    <div class="footer-desc">Our passion drives us to create meaningful experiences and exceed expectations every step of the way.</div>
    <div class="col" style="left:230px"><b>DISCOVER</b>Our Project<br>About Us<br>Solutions<br>Testimonials<br>Our Team</div>
    <div class="col" style="left:310px"><b>CONTACT</b>Contact Us<br>FAQs<br>Privacy Policy<br>Terms of Service</div>
    <div class="col" style="left:403px"><b>RESOURCES</b>Blog<br>Partners<br>Careers<br>Customer Support</div>
    <div class="col" style="left:503px"><b>FOLLOW US</b>Snapframe<br>Chirpline<br>Circlebook<br>Workweave</div>
    <div class="rule"></div>
    <div class="copy">© 2023 Kindred Path Project. All rights reserved.</div>
  </footer>

</div>
</body>
</html>
```